Ochre Ridge Critters business card and social media card

I would like 2 designs,

one with my logo that I have (attached file) for the front and then the chatterbook, Snapwall and roamrater icons on the back.I would like it to be eye catching.

The second design i would like the designers to come up with.I am looking for a colorful and eye catching but easy to read business card. I am in the center of Australia and would like earthy colors like orange/red, yellow, charcoal, brown, green etc. I would like a blue tongue lizard and a king brown snake in the design for the front. For the back I would like the Chatterbook, Snapwall and roam rater logos.

Industry/Entity Type

Business

Contact Information for Business Card

Milo Farrant
CEO
OCHRE RIDGE CRITTERS pty ltd
W: 041 902 7364
M: 048 516 2097
E: milo@ochreridgecritters.com.au

Font styles to use
Other font styles liked:
• chiller

Colors
f37122
fbed22
ec1f27
474747
0492cd
acd036

Requirements
Must have
• Business name or my logo (attached file)
• Ochre Ridge Critters (in a cool font, like "chiller")
• Chatterbook icon
• Snapwall icon
• Roamrater icon
Nice to have
• Snake and a blue tongue lizard (either the full animals or just the heads)

```html
<!DOCTYPE html>
<html lang="en">
<head>
<meta charset="utf-8">
<title>Ochre Ridge Critters – Business Card</title>
<link rel="stylesheet" href="https://fonts.googleapis.com/css2?family=Permanent+Marker&family=Patrick+Hand&display=swap">
<style>
  :root {
    --backdrop: #2b2b2b;
    --card-red: #d1283a;
    --card-white: #ffffff;
    --ink: #1a1a1a;
    --accent-red: #ec1f27;
    --accent-orange: #f7941d;
    --line-white: #f4e9e9;
    --line-dark: #474747;
  }
  * { box-sizing: border-box; margin: 0; padding: 0; }
  html, body { width: 1200px; height: 852px; overflow: hidden; }
  body {
    background: var(--backdrop);
    font-family: "Patrick Hand", "Comic Sans MS", cursive;
    position: relative;
  }
  .card {
    position: absolute;
    width: 520px;
    height: 300px;
    border-radius: 22px;
    box-shadow: 0 10px 30px rgba(0,0,0,.45);
    overflow: hidden;
  }
  .card--back { left: 60px; top: 276px; background: var(--card-red); }
  .card--front { left: 620px; top: 276px; background: var(--card-white); }

  /* Logo: plain mark + stacked name, centred */
  .logo {
    position: absolute;
    display: flex;
    align-items: center;
    gap: 14px;
    transform: translateX(-50%);
  }
  .logo__mark {
    width: 34px; height: 34px; border-radius: 50%;
    background: var(--accent-orange);
    flex: none;
  }
  .logo__name {
    font-family: "Permanent Marker", "Comic Sans MS", cursive;
    font-size: 28px;
    line-height: 1.02;
    letter-spacing: 1px;
    text-transform: uppercase;
  }
  .logo__name span { display: block; }
  .card--back .logo { left: 260px; top: 56px; }
  .card--back .logo__name { color: var(--card-white); }
  .card--front .logo { left: 240px; top: 34px; }
  .card--front .logo__name { color: var(--accent-red); }

  .rule { position: absolute; height: 1px; }

  /* Back: social row */
  .card--back .rule { left: 96px; right: 44px; top: 262px; background: var(--line-white); }
  .social__item {
    position: absolute;
    display: flex; align-items: center; gap: 5px;
    color: var(--card-white);
    font-size: 13px;
    line-height: 1;
  }
  .social__dot { width: 18px; height: 18px; border-radius: 50%; background: var(--card-white); flex: none; }
  .social__item--chatter { left: 18px; top: 244px; }
  .social__item--snap { left: 18px; top: 268px; }
  .social__item--roam { right: 18px; top: 236px; }

  /* Front */
  .card--front .rule--top { left: 380px; right: 26px; top: 96px; background: var(--line-dark); }
  .card--front .rule--bottom { left: 24px; right: 24px; top: 250px; background: var(--line-dark); }

  .person {
    position: absolute;
    right: 40px; top: 176px;
    text-align: center;
    width: 180px;
  }
  .person__name {
    font-family: "Permanent Marker", "Comic Sans MS", cursive;
    font-size: 19px; color: var(--ink); letter-spacing: 1px; line-height: 1.1;
  }
  .person__role { font-size: 12px; color: var(--accent-red); letter-spacing: 2px; line-height: 1; }

  .contact {
    position: absolute;
    left: 24px; top: 258px;
    font-size: 14px;
    font-weight: 700;
    color: var(--ink);
    white-space: nowrap;
    word-spacing: 1px;
  }
</style>
</head>
<body>
  <section class="card card--back" aria-label="Card back">
    <div class="logo">
      <span class="logo__mark"></span>
      <p class="logo__name"><span>Ochre</span><span>Ridge</span><span>Critters</span></p>
    </div>
    <div class="rule"></div>
    <span class="social__item social__item--chatter"><span class="social__dot"></span>Chatterbook</span>
    <span class="social__item social__item--snap"><span class="social__dot"></span>Snapwall</span>
    <span class="social__item social__item--roam"><span class="social__dot"></span>Roamrater</span>
  </section>

  <section class="card card--front" aria-label="Card front">
    <div class="rule rule--top"></div>
    <div class="logo">
      <span class="logo__mark"></span>
      <p class="logo__name"><span>Ochre</span><span>Ridge</span><span>Critters</span></p>
    </div>
    <div class="person">
      <p class="person__name">MILO FARRANT</p>
      <p class="person__role">CEO</p>
    </div>
    <div class="rule rule--bottom"></div>
    <p class="contact">W. 041 902 7364 &nbsp;M. 048 516 2097 &nbsp;E. milo@ochreridgecritters.com.au</p>
  </section>
</body>
</html>
```